Wallpaper für Partner für ganzheitliche IT-Infrastruktur-Lösungen
Zielgruppe
Wir sind Partner für ganzheitliche IT-Infrastruktur-Lösungen. Wir übernehmen technische Verantwortung für stabile, sichere und wirtschaftliche IT‑Systeme – von der Konzeption über den Betrieb bis zur langfristigen Betreuung. Unsere Zielgruppe sind kleine und mittelständische Unternehmen und Organisationen, die ihre IT als strategischen Erfolgsfaktor verstehen und Wert auf durchdachte Gesamtlösungen statt auf Stückwerk legen.
Aufgabenstellung
Es soll ein Wallpaper erstellt werden, das die bestehende CI ergänzt.
Das Design soll Verantwortung, Kompetenz und Verlässlichkeit ausstrahlen. Gesucht ist eine professionelle, aber zugängliche Optik, die ganzheitliches Denken und technische Stabilität vermittelt. Der Stil sollte modern, aber zeitlos sein – keine kurzlebigen Trends oder oberflächliche Tech-Klischees. Wichtig sind klare Strukturen und hochwertige Ästhetik, die Vertrauen schafft. Das NK-VR-Logo oder -Icon soll harmonisch in das Design integriert werden. Technische Anforderungen: Der Wallpaper muss sowohl im 16:9- als auch im 9:16-Format funktionieren und vollständig als Vektorgrafik ohne Rastereffekte geliefert werden.

```html
<!DOCTYPE html>
<html lang="de">
<head>
<meta charset="utf-8">
<title>NK-VR GmbH – Wallpaper</title>
<link rel="stylesheet" href="https://fonts.googleapis.com/css2?family=Titillium+Web:wght@300;600;700&display=swap">
<style>
  :root {
    --stage: #e0e0e0;
    --brand-red: #b71c23;
    --soft-pink: #e2a5a8;
    --deep-rust: #c03a30;
    --white: #ffffff;
  }
  html, body {
    margin: 0;
    width: 1200px;
    height: 1117px;
    overflow: hidden;
    background: var(--stage);
  }
  .wallpaper {
    position: absolute;
    left: 40px;
    top: 243px;
    width: 1120px;
    height: 630px;
    display: block;
  }
  .fill-red { fill: var(--brand-red); }
  .fill-pink { fill: var(--soft-pink); }
  .fill-rust { fill: var(--deep-rust); }
  .fill-white { fill: var(--white); }
  .web-address {
    font-family: "Titillium Web", sans-serif;
    font-weight: 600;
    font-size: 44px;
    letter-spacing: 20px;
    fill: var(--brand-red);
  }
  .brand-name {
    font-family: "Titillium Web", sans-serif;
    font-weight: 300;
    font-size: 190px;
    fill: var(--white);
  }
  .brand-suffix {
    font-family: "Titillium Web", sans-serif;
    font-weight: 300;
    font-size: 52px;
    fill: var(--white);
  }
  .service-frame {
    fill: none;
    stroke: var(--soft-pink);
    stroke-width: 6;
  }
  .service-label {
    font-family: "Titillium Web", sans-serif;
    font-weight: 700;
    font-size: 34px;
    fill: var(--white);
    text-anchor: middle;
  }
  .icon-line {
    fill: none;
    stroke: var(--white);
    stroke-width: 7;
    stroke-linecap: round;
  }
</style>
</head>
<body>
<svg class="wallpaper" viewBox="0 0 1795 1009" xmlns="http://www.w3.org/2000/svg">
  <defs>
    <pattern id="dot-grid" x="0" y="0" width="24.5" height="25" patternUnits="userSpaceOnUse">
      <rect width="9" height="9" class="fill-pink"/>
    </pattern>
    <clipPath id="card-area"><rect width="1795" height="1009"/></clipPath>
  </defs>

  <g clip-path="url(#card-area)">
    <rect class="fill-red" width="1795" height="1009"/>

    <!-- upper left band -->
    <rect class="fill-pink" x="-40" y="-40" width="837" height="191" rx="33"/>

    <!-- vertical address column -->
    <rect class="fill-pink" x="91" y="0" width="266" height="1060" rx="33"/>
    <rect class="fill-red" x="-60" y="84" width="151" height="1000" rx="33"/>
    <rect class="fill-red" x="-60" y="151" width="220" height="174" rx="33"/>
    <rect class="fill-red" x="290" y="151" width="150" height="174" rx="33"/>
    <rect class="fill-red" x="-60" y="591" width="220" height="174" rx="33"/>
    <rect class="fill-red" x="290" y="591" width="150" height="174" rx="33"/>
    <rect class="fill-red" x="357" y="84" width="174" height="140" rx="33"/>

    <!-- right edge band -->
    <rect class="fill-pink" x="1682" y="-40" width="160" height="191" rx="33"/>
    <rect class="fill-pink" x="1676" y="253" width="160" height="800" rx="33"/>
    <rect class="fill-red" x="1640" y="519" width="105" height="174" rx="33"/>
    <rect class="fill-red" x="1640" y="959" width="105" height="120" rx="33"/>

    <!-- floating blocks -->
    <rect class="fill-pink" x="532" y="247" width="267" height="267" rx="33"/>
    <rect class="fill-pink" x="436" y="560" width="147" height="147" rx="18"/>

    <!-- bottom base strip -->
    <rect class="fill-rust" x="426" y="904" width="1146" height="160" rx="33"/>
    <rect class="fill-red" x="692" y="860" width="174" height="113" rx="33"/>
    <rect class="fill-red" x="1132" y="860" width="173" height="113" rx="33"/>

    <!-- dot grids -->
    <g transform="translate(881 109)"><rect fill="url(#dot-grid)" width="183" height="34"/></g>
    <g transform="translate(1704 181)"><rect fill="url(#dot-grid)" width="83" height="34"/></g>
    <g transform="translate(436 795)"><rect fill="url(#dot-grid)" width="183" height="34"/></g>
  </g>

  <!-- web address -->
  <text class="web-address" transform="translate(244 706) rotate(-90)">NK-VR.COM</text>

  <!-- brand name -->
  <rect class="fill-white" x="876" y="314" width="124" height="124" rx="12"/>
  <text class="brand-name" x="1046" y="438" textLength="420" lengthAdjust="spacingAndGlyphs">NK-VR</text>
  <text class="brand-suffix" x="1488" y="438" textLength="112" lengthAdjust="spacingAndGlyphs">GmbH</text>

  <!-- service: managed services -->
  <g class="service">
    <rect class="service-frame" x="876" y="558" width="157" height="158" rx="22"/>
    <rect class="icon-line" x="940" y="600" width="28" height="18" rx="4"/>
    <line class="icon-line" x1="954" y1="618" x2="954" y2="636"/>
    <line class="icon-line" x1="906" y1="636" x2="1002" y2="636"/>
    <line class="icon-line" x1="930" y1="636" x2="930" y2="650"/>
    <line class="icon-line" x1="978" y1="636" x2="978" y2="650"/>
    <rect class="icon-line" x="916" y="652" width="28" height="18" rx="4"/>
    <rect class="icon-line" x="964" y="652" width="28" height="18" rx="4"/>
    <text class="service-label" x="954" y="770">MANAGED</text>
    <text class="service-label" x="954" y="803">SERVICES</text>
  </g>

  <!-- service: managed infrastructure -->
  <g class="service">
    <rect class="service-frame" x="1156" y="558" width="157" height="158" rx="22"/>
    <rect class="fill-white" x="1190" y="593" width="89" height="37" rx="18.5"/>
    <rect class="fill-white" x="1190" y="643" width="89" height="37" rx="18.5"/>
    <circle class="fill-red" cx="1250" cy="611" r="5"/>
    <circle class="fill-red" cx="1264" cy="611" r="5"/>
    <circle class="fill-red" cx="1250" cy="661" r="5"/>
    <circle class="fill-red" cx="1264" cy="661" r="5"/>
    <text class="service-label" x="1234" y="766">MANAGED</text>
    <text class="service-label" x="1234" y="799">INFRASTRUKTUR</text>
  </g>

  <!-- service: consulting -->
  <g class="service">
    <rect class="service-frame" x="1446" y="558" width="157" height="158" rx="22"/>
    <circle class="fill-white" cx="1524" cy="622" r="29"/>
    <rect class="fill-white" x="1510" y="640" width="28" height="22"/>
    <path class="fill-white" d="M1509 668 h30 v4 a15 15 0 0 1 -30 0 z"/>
    <path d="M1508 622 a15 15 0 0 1 14 -15" fill="none" stroke="var(--brand-red)" stroke-width="5" stroke-linecap="round"/>
    <line class="icon-line" x1="1480" y1="622" x2="1488" y2="622"/>
    <line class="icon-line" x1="1560" y1="622" x2="1568" y2="622"/>
    <line class="icon-line" x1="1481" y1="600" x2="1488" y2="604"/>
    <line class="icon-line" x1="1567" y1="600" x2="1560" y2="604"/>
    <line class="icon-line" x1="1481" y1="644" x2="1488" y2="640"/>
    <line class="icon-line" x1="1567" y1="644" x2="1560" y2="640"/>
    <text class="service-label" x="1524" y="786">IT-CONSULTING</text>
  </g>
</svg>
</body>
</html>
```